Customer Loyalty Card - Tourism - Tour Card

We would like to make a loyalty card for our tour business. If someone books 1 full priced tour they then get 10% off the 2nd tour and 10% off the 3rd tour and 15% off the 4th tour they do with us. All bookings must be booked directly with Kestrel Bay Wildlife Tours

View our website for design and colour ideas www.kestrelbaywildlifetours.com

Target Market(s)

People on holidays doing tours on Lord Howe Island

Industry/Entity Type

Travel

Contact Information for Business Card

www.kestrelbaywildlifetours.com
Im looking for a 1 sided card - if possible.

Phone, email and address are probably not really required. I will need to stamp the card once a tour has been booked and paid for. There is no name and position, its just a business card sized Loyalty Card.

Requirements
Must have
• Logo
• I will need to stamp the card once a tour has been booked and paid for.

```html
<!DOCTYPE html>
<html lang="en">
<head>
<meta charset="utf-8">
<title>Kestrel Bay Wildlife Tours – Loyalty Card</title>
<link rel="stylesheet" href="https://fonts.googleapis.com/css2?family=Oswald:wght@500;600&family=Roboto:wght@400&family=Dancing+Script:wght@600&display=swap">
<style>
  :root {
    --bg: #3a3a3b;
    --orange: #f09e30;
    --teal: #24677a;
    --white: #ffffff;
    --ink: #1e1718;
    --text: #444444;
  }
  * { margin: 0; padding: 0; box-sizing: border-box; }
  html, body { width: 1200px; height: 1000px; overflow: hidden; background: var(--bg); }
  .stage { position: relative; width: 1200px; height: 1000px; }
  .card {
    position: absolute; left: 150px; top: 230px; width: 900px; height: 540px;
    background: var(--white); overflow: hidden;
    font-family: "Roboto", Arial, sans-serif;
  }
  .band { position: absolute; left: 0; width: 100%; }
  .band--orange-top { top: 0; height: 110px; background: var(--orange); }
  .band--stripe { height: 13px; background: var(--white); }
  .band--stripe-1 { top: 30px; }
  .band--stripe-2 { top: 75px; }
  .band--teal-main { top: 150px; height: 180px; background: var(--teal); }
  .band--stripe-low { top: 445px; height: 12px; background: var(--white); }
  .band--orange-address { top: 457px; height: 50px; background: var(--orange); }
  .band--teal-foot { top: 507px; height: 33px; background: var(--teal); }

  .brand-tag {
    position: absolute; left: 20px; top: 98px; height: 56px; padding: 0 20px 0 12px;
    background: var(--ink); display: flex; align-items: center; gap: 12px;
  }
  .brand-tag__dot { width: 40px; height: 40px; border-radius: 50%; background: var(--orange); flex: none; }
  .brand-tag__name {
    font-family: "Oswald", Arial, sans-serif; font-weight: 600; color: var(--white);
    font-size: 17px; line-height: 1.1; text-transform: uppercase; letter-spacing: .5px;
  }

  .title {
    position: absolute; left: 190px; top: 182px;
    font-family: "Oswald", Arial, sans-serif; font-weight: 600; font-size: 38px;
    color: var(--white); text-transform: uppercase; letter-spacing: .5px;
    text-shadow: 2px 3px 4px rgba(0,0,0,.45);
  }
  .subtitle {
    position: absolute; left: 560px; top: 228px;
    font-family: "Dancing Script", cursive; font-weight: 600; font-size: 32px;
    color: var(--orange);
  }

  .side-block { position: absolute; left: 0; top: 330px; width: 70px; height: 115px; background: var(--teal); }
  .stamp-panel { position: absolute; left: 410px; top: 272px; width: 490px; height: 168px; background: var(--teal); }
  .stamp-panel svg { position: absolute; left: 0; top: -50px; }
  .notch { position: absolute; left: 340px; top: 440px; }

  .contacts { position: absolute; left: 115px; top: 355px; list-style: none; }
  .contacts li { display: flex; align-items: center; gap: 12px; font-size: 17px; color: var(--text); height: 32px; }
  .contacts svg { flex: none; }

  .address {
    position: absolute; left: 0; top: 457px; width: 100%; height: 50px;
    display: flex; align-items: center; justify-content: center; gap: 8px;
    font-size: 18px; color: var(--text);
  }
</style>
</head>
<body>
<main class="stage">
  <section class="card" aria-label="Kestrel Bay Wildlife Tours loyalty card">
    <div class="band band--orange-top"></div>
    <div class="band band--stripe band--stripe-1"></div>
    <div class="band band--stripe band--stripe-2"></div>
    <div class="band band--teal-main"></div>
    <div class="band band--stripe-low"></div>
    <div class="band band--orange-address"></div>
    <div class="band band--teal-foot"></div>

    <div class="brand-tag">
      <span class="brand-tag__dot"></span>
      <span class="brand-tag__name">Kestrel Bay<br>Wildlife Tours</span>
    </div>

    <h1 class="title">Kestrel Bay Wildlife Tours</h1>
    <p class="subtitle">Loyalty card</p>

    <div class="side-block"></div>

    <div class="stamp-panel" aria-label="Stamp spaces">
      <svg width="490" height="230" viewBox="0 0 490 230">
        <defs>
          <polygon id="stamp-star" points="0,-60 14,-19 57,-19 22,7 35,49 0,23 -35,49 -22,7 -57,-19 -14,-19"/>
        </defs>
        <g fill="#ffffff">
          <use href="#stamp-star" x="90" y="120"/>
          <use href="#stamp-star" x="225" y="165"/>
          <use href="#stamp-star" x="345" y="130"/>
          <use href="#stamp-star" x="420" y="58"/>
        </g>
      </svg>
    </div>
    <svg class="notch" width="40" height="18" viewBox="0 0 40 18"><polygon points="0,0 40,0 20,18" fill="#24677a"/></svg>

    <ul class="contacts">
      <li>
        <svg width="18" height="22" viewBox="0 0 18 22" fill="none" stroke="#24677a" stroke-width="1.6"><rect x="3" y="1" width="12" height="20" rx="2"/><line x1="7" y1="17" x2="11" y2="17"/></svg>
        0255 418 730
      </li>
      <li>
        <svg width="20" height="16" viewBox="0 0 20 16" fill="none" stroke="#24677a" stroke-width="1.6"><rect x="1" y="2" width="18" height="12"/><polyline points="1,2 10,9 19,2"/></svg>
        info@kestrelbaywildlifetours.com
      </li>
      <li>
        <svg width="20" height="20" viewBox="0 0 20 20" fill="none" stroke="#24677a" stroke-width="1.5"><circle cx="10" cy="10" r="8.5"/><ellipse cx="10" cy="10" rx="4" ry="8.5"/><line x1="1.5" y1="10" x2="18.5" y2="10"/></svg>
        www.kestrelbaywildlifetours.com
      </li>
    </ul>

    <p class="address">
      <svg width="14" height="20" viewBox="0 0 14 20" fill="none" stroke="#444" stroke-width="1.5"><path d="M7 19 C7 19 1 11 1 7 A6 6 0 0 1 13 7 C13 11 7 19 7 19 Z"/><circle cx="7" cy="7" r="2.2"/></svg>
      Boatshed 4, Harbour foreshore - opposite Marlin Cycle Rentals, Kestrel Bay NSW 2871
    </p>
  </section>
</main>
</body>
</html>
```